Healthcare website - Diabetic Shoes - Elderfund - No Cost

I am looking to upgrade my website. I do not want to use Wordpress, Adobe Muse or another designing program. The code should be easily editable using textpad or VI. After the project is done I want to easily add my custom PHP code.

Features
Creative and Modern Design .
Fully responsive site for use on mobile devices
bootstrap, jquery

My current website is
www.pebblewalkco.com

Target Market(s)

Older people who have diabetes. Target market is +60 years old, but we do have younger people going to the site to help out their parents.

Industry/Entity Type

Healthcare

Coding

Coded - Design and coding required

Number of Pages Required

2 page

Colors

Designer to choose colors to be used in the design.

Requirements
Must have
• The code should be easily editable using textpad or VI. After the project is done I want to easily add my custom PHP code.
• The first page will be the home page and the other page I need is this form.
• https://www.pebblewalkco.com/pebble-walk-co-do-i-qualify.php
Should not have
• I do not want to use Wordpress, Adobe Muse or another designing program.

```html
<!DOCTYPE html>
<html lang="en">
<head>
<meta charset="utf-8">
<title>Pebble Walk Co — Diabetic Shoes Covered by Elderfund</title>
<link href="https://fonts.googleapis.com/css2?family=Roboto:wght@300;400;500;700&display=swap" rel="stylesheet">
<style>
:root{
  --blue:#2a9bd8;
  --blue-dark:#2f6fa6;
  --green:#6cc063;
  --green-soft:#7dc771;
  --green-pale:#e6f5e3;
  --ink:#2b2b2b;
  --muted:#777;
  --line:#e4e4e4;
  --dark:#1f1f1f;
  --darker:#151515;
  --white:#fff;
}
*{box-sizing:border-box;margin:0;padding:0}
html,body{width:1200px;height:3586px;overflow:hidden}
body{font-family:"Roboto",Arial,sans-serif;color:var(--ink);background:var(--white);position:relative}
.page{position:relative;width:1200px;height:3586px}

/* header */
.topbar{position:absolute;top:0;left:0;width:1200px;height:72px}
.brand{position:absolute;left:88px;top:22px;display:flex;align-items:center;gap:10px;font-size:26px;font-weight:500;color:var(--blue-dark)}
.brand-dot{width:14px;height:14px;border-radius:50%;background:var(--green)}
.social{position:absolute;left:720px;top:20px;display:flex;gap:8px}
.social span{width:26px;height:26px;border:1px solid #ccc;border-radius:50%}
.call{position:absolute;left:808px;top:14px;display:flex;align-items:center;gap:10px}
.call small{display:block;font-size:11px;color:var(--muted)}
.call strong{font-size:19px;color:var(--blue-dark);font-weight:500}
.chat{position:absolute;left:988px;top:18px;width:124px;height:36px;border:2px solid var(--green);border-radius:20px;display:flex;align-items:center;gap:8px;padding-left:8px;font-size:12px;font-weight:700;color:var(--green)}
.chat i{width:22px;height:22px;border-radius:50%;background:var(--green)}
.nav{position:absolute;top:72px;left:0;width:1200px;height:43px;border-top:1px solid var(--line);display:flex;align-items:center;padding-left:88px}
.nav a{font-size:14px;color:var(--ink);text-decoration:none;margin-right:30px;height:43px;line-height:43px}
.nav a.active{color:var(--blue);border-bottom:3px solid var(--blue)}
.nav .login{position:absolute;right:88px;top:0;background:var(--blue);color:#fff;padding:0 26px;margin:0;font-weight:500}

/* hero */
.hero{position:absolute;top:115px;left:0;width:1200px;height:566px;background:linear-gradient(180deg,#f4f4f4,#dcdcdc)}
.hero-mark{position:absolute;left:88px;top:147px;display:flex;align-items:center;gap:10px;font-size:24px;font-weight:500;color:#555;letter-spacing:2px}
.hero-mark i{width:22px;height:22px;background:#555}
.hero-tag{position:absolute;left:88px;top:247px;background:var(--blue-dark);color:#fff;font-size:19px;padding:8px 14px}
.hero h1{position:absolute;left:88px;top:296px;font-size:44px;font-weight:700;color:var(--blue-dark)}
.hero p{position:absolute;left:88px;top:356px;width:560px;font-size:14px;line-height:22px;color:#444}
.hero-photo{position:absolute;left:520px;top:30px;width:620px;height:460px;border-radius:40px;background:radial-gradient(ellipse at center,#6b4a36 0%,#3b3b3b 45%,rgba(120,120,120,.2) 75%,transparent 80%)}
.arrow{position:absolute;top:262px;width:36px;height:36px;border-radius:50%;background:#fff;border:1px solid #ccc;display:flex;align-items:center;justify-content:center}
.down{position:absolute;left:584px;top:525px;width:30px;height:30px;border-radius:50%;border:1px solid #888;display:flex;align-items:center;justify-content:center}

/* about */
.about{position:absolute;top:681px;left:0;width:1200px;height:489px}
.about h2{position:absolute;left:88px;top:147px;font-size:28px;font-weight:400}
.about p{position:absolute;left:88px;top:192px;width:595px;font-size:12.5px;line-height:21px;color:var(--muted)}
.pill{display:inline-block;background:var(--green-pale);color:var(--green);border-radius:22px;font-size:12px;padding:12px 26px}
.about .pill{position:absolute;left:88px;top:317px}
.about-frame{position:absolute;left:750px;top:157px;width:244px;height:250px;border:5px solid var(--green);border-top:none;border-right:none}
.about-frame::after{content:"";position:absolute;right:-5px;top:0;width:5px;height:0}
.about-photo{position:absolute;left:782px;top:72px;width:330px;height:310px;background:linear-gradient(180deg,#8fc3e8 0%,#c9d9e4 45%,#4b8a43 100%)}

/* steps */
.steps{position:absolute;top:1170px;left:0;width:1200px;height:347px;background:var(--blue);color:#fff}
.steps h2{position:absolute;top:62px;width:1200px;text-align:center;font-size:27px;font-weight:400}
.steps .rule{position:absolute;left:588px;top:108px;width:24px;height:2px;background:#fff}
.step{position:absolute;top:135px;width:230px;text-align:center}
.step .icon{width:94px;height:94px;border-radius:50%;background:rgba(255,255,255,.15);margin:0 auto;display:flex;align-items:center;justify-content:center}
.step .icon.on{background:var(--green);box-shadow:0 0 0 8px rgba(255,255,255,.2)}
.step p{margin-top:26px;font-size:13px;line-height:21px}

/* products */
.products{position:absolute;top:1517px;left:0;width:1200px;height:561px}
.products h2{position:absolute;top:67px;width:1200px;text-align:center;font-size:27px;font-weight:400}
.products .rule{position:absolute;left:588px;top:110px;width:24px;height:2px;background:var(--blue)}
.card{position:absolute;top:135px;width:243px;height:258px;border:1px solid var(--line);background:#fff}
.card.hover{background:#f4f4f4;box-shadow:0 6px 18px rgba(0,0,0,.12)}
.card .shot{position:absolute;left:50px;top:24px;width:143px;height:150px;border-radius:10px}
.card h3{position:absolute;left:14px;top:196px;font-size:12px;font-weight:500}
.card p{position:absolute;left:14px;top:216px;width:215px;font-size:11.5px;color:var(--muted);white-space:nowrap;overflow:hidden;text-overflow:ellipsis}
.products .pill{position:absolute;left:518px;top:444px}

/* video */
.video{position:absolute;top:2078px;left:0;width:1200px;height:432px;background:var(--green-soft)}
.video-art{position:absolute;left:60px;top:20px;width:1000px;height:400px;background:linear-gradient(120deg,rgba(255,255,255,.12),rgba(255,255,255,.04))}
.play{position:absolute;left:562px;top:174px;width:76px;height:76px;border-radius:50%;background:#fff;display:flex;align-items:center;justify-content:center}

/* faq */
.faq{position:absolute;top:2510px;left:0;width:1200px;height:520px}
.faq .track{position:absolute;left:112px;top:55px;width:1px;height:400px;background:var(--line)}
.faq-item{position:absolute;left:138px;font-size:17px;color:var(--ink)}
.faq-item::before{content:"";position:absolute;left:-31px;top:6px;width:10px;height:10px;border-radius:50%;border:1px solid #bbb;background:#fff}
.faq-open{position:absolute;left:88px;top:112px;width:590px;height:330px;background:#fff;box-shadow:0 4px 20px rgba(0,0,0,.12);border-left:3px solid var(--blue);padding:22px 26px 0 46px}
.faq-open h3{font-size:17px;font-weight:500;margin-bottom:14px;position:relative}
.faq-open h3::before{content:"";position:absolute;left:-31px;top:5px;width:10px;height:10px;border-radius:50%;border:2px solid var(--blue)}
.faq-open p{font-size:12.5px;line-height:21px;color:#555;margin-bottom:10px}
.faq-photo{position:absolute;left:729px;top:0;width:471px;height:520px;background:linear-gradient(180deg,#f2f2f2,#e4e4e4)}
.faq-photo::after{content:"";position:absolute;left:60px;top:190px;width:360px;height:150px;border-radius:60px 80px 30px 30px;background:#2e4a8a}

/* catalog form */
.catalog{position:absolute;top:3030px;left:0;width:1200px;height:502px;background:var(--dark);color:#fff}
.catalog h2{position:absolute;top:68px;width:1200px;text-align:center;font-size:27px;font-weight:400}
.field{position:absolute;font-size:12px;color:#ccc;border-bottom:1px solid #555;height:30px}
.field.select::after{content:"";position:absolute;right:6px;top:4px;width:6px;height:6px;border-right:1px solid #aaa;border-bottom:1px solid #aaa;transform:rotate(45deg)}
.catalog .btn{position:absolute;left:530px;top:400px;width:140px;height:44px;border-radius:22px;background:var(--green);color:#fff;font-size:12px;text-align:center;line-height:44px}

.bottombar{position:absolute;top:3532px;left:0;width:1200px;height:54px;background:var(--darker);color:#aaa;font-size:11.5px}
.bottombar .copy{position:absolute;left:88px;top:20px}
.bottombar .links{position:absolute;right:88px;top:20px;word-spacing:4px}
.totop{position:absolute;left:1133px;top:3512px;width:34px;height:34px;border-radius:50%;background:var(--blue);display:flex;align-items:center;justify-content:center}
</style>
</head>
<body>
<div class="page">

<header class="topbar">
  <div class="brand"><span class="brand-dot"></span>Pebble Walk Co</div>
  <div class="social"><span></span><span></span><span></span></div>
  <div class="call">
    <svg width="18" height="34" viewBox="0 0 18 34"><rect x="1" y="1" width="16" height="32" rx="3" fill="none" stroke="#555" stroke-width="2"/><circle cx="9" cy="28" r="1.5" fill="#555"/></svg>
    <div><small>Call us!</small><strong>1-800-555-0142</strong></div>
  </div>
  <div class="chat"><i></i>LIVE CHAT</div>
</header>

<nav class="nav">
  <a class="active" href="#">Home</a><a href="#">About</a><a href="#">Video</a><a href="#">Pebble Walk Co! Do I Qualify!</a><a href="#">Why Diabetic Shoes?</a><a href="#">Shoes</a><a href="#">Products</a><a href="#">Shoe Fitter Jobs</a><a href="#">FAQ</a>
  <a class="login" href="#">LOGIN</a>
</nav>

<section class="hero">
  <div class="hero-photo" role="img" aria-label="Four diabetic shoes and sneakers in brown, black and grey"></div>
  <div class="hero-mark"><i></i>STRIDEWELL</div>
  <div class="hero-tag">Diabbetic Shoes Or Sneakers</div>
  <h1>COVERED BY ELDERFUND</h1>
  <p>No or little out of pocket Cost To You!* Elderfund, and most insurance plans, may cover the cost of one pair of diabetic shoes and three pairs of custom inserts per calendar year.Co-payments, deductibles and some restrictions apply.</p>
  <div class="arrow" style="left:24px"><svg width="10" height="12"><path d="M8 1 2 6l6 5" fill="none" stroke="#555" stroke-width="1.5"/></svg></div>
  <div class="arrow" style="left:1138px"><svg width="10" height="12"><path d="M2 1l6 5-6 5" fill="none" stroke="#555" stroke-width="1.5"/></svg></div>
  <div class="down"><svg width="12" height="8"><path d="M1 1l5 5 5-5" fill="none" stroke="#666" stroke-width="1.5"/></svg></div>
</section>

<section class="about">
  <h2>About Us</h2>
  <p>Pebble Walk Co was created by Harbor Lane Medical Supply to educate clients and prospective shoe fitters about diabetic shoes and the coverage that Elderfund provides. Founded by a Board-Certified Pedorthist, the company's mission is to help clients receive properly fitted shoes from qualified healthcare professionals around the United States. Harbor Lane Medical Supply works directly with Elderfund to determine the patient's coverage.</p>
  <a class="pill">Learn More</a>
  <div class="about-frame"></div>
  <div class="about-photo" role="img" aria-label="Modern office building with palm trees"></div>
</section>

<section class="steps">
  <h2>4 Easy Steps To Receive Your New Therapeutic Shoes.</h2>
  <div class="rule"></div>
  <div class="step" style="left:65px"><div class="icon"><svg width="30" height="38" viewBox="0 0 30 38"><path d="M2 2h18l8 8v26H2z" fill="none" stroke="#fff" stroke-width="2"/><path d="M8 16h14M8 22h14M8 28h10" stroke="#fff" stroke-width="2"/></svg></div><p>Fill out an application to see<br>if you qualify.</p></div>
  <div class="step" style="left:347px"><div class="icon on"><svg width="30" height="38" viewBox="0 0 30 38"><rect x="2" y="5" width="26" height="31" fill="none" stroke="#fff" stroke-width="2"/><rect x="9" y="1" width="12" height="7" fill="#fff"/><path d="M8 18h14M8 24h14M8 30h10" stroke="#fff" stroke-width="2"/></svg></div><p>A prescription will befaxed to your<br>primary physician</p></div>
  <div class="step" style="left:630px;width:240px"><div class="icon"><svg width="44" height="24" viewBox="0 0 44 24"><path d="M2 20V8c6 0 10-6 14-6 2 6 10 8 18 10 6 2 8 5 8 8z" fill="none" stroke="#fff" stroke-width="2"/><path d="M2 22h40" stroke="#fff" stroke-width="2"/></svg></div><p>After the prescription is signed, a certified<br>shoe fitter will fit your new shoes.</p></div>
  <div class="step" style="left:912px"><div class="icon"><svg width="36" height="36" viewBox="0 0 36 36"><path d="M6 34V4h24v30M6 14h24" fill="none" stroke="#fff" stroke-width="2"/><circle cx="18" cy="8" r="3" fill="#fff"/></svg></div><p>Enjoy your new shoes!</p></div>
</section>

<section class="products">
  <h2>Click Here For Our Elderfund Products</h2>
  <div class="rule"></div>
  <div class="card" style="left:88px"><div class="shot" role="img" aria-label="TENS unit with electrode pads" style="background:linear-gradient(180deg,#555,#ccc)"></div><h3>Tens Unit</h3><p>A Transcutaneous Electrical Nerve Stimulation</p></div>
  <div class="card" style="left:348px"><div class="shot" role="img" aria-label="Portable seat lift cushion" style="background:linear-gradient(180deg,#333,#888)"></div><h3>Seat Lift</h3><p>Electric-powered portable seat assist cushion</p></div>
  <div class="card hover" style="left:607px"><div class="shot" role="img" aria-label="Lumbar back brace" style="background:linear-gradient(180deg,#7ab6e0,#3c5a78)"></div><h3>Back Brace</h3><p>The FlexaCore Pro lumbar sacral support</p></div>
  <div class="card" style="left:866px"><div class="shot" role="img" aria-label="Knee, wrist and ankle braces" style="background:linear-gradient(180deg,#222,#666)"></div><h3>Knee, Ankle, Wrist, Braces</h3><p>Our knees are susceptible to injuries every day</p></div>
  <a class="pill">View All Our Products</a>
</section>

<section class="video">
  <div class="video-art" role="img" aria-label="Line illustration of a man at a laptop with forms and a shoe"></div>
  <div class="play"><svg width="24" height="28"><path d="M3 2l20 12L3 26z" fill="var(--blue)"/></svg></div>
</section>

<section class="faq">
  <div class="track"></div>
  <div class="faq-item" style="top:58px">How Does Diabetes Cause Foot Problems?</div>
  <div class="faq-open">
    <h3>Why Are Properly Fitted Shoes Important?</h3>
    <p>Twenty four million people have diabetes, and twenty-five percent of this population will develop foot problems caused by their disease. We provide the most fashionable orthopedic shoes available, in a variety of styles and brands, to help treat and prevent painful diabetic symptoms.</p>
    <p>Our orthopedic shoes reduce the pressure and friction on your feet that can lead to foot injuries. Custom inserts relieve pressure and cushion your feet. Diabetic Socks and our therapeutic shoes are also accurately sized and padded to ensure that there is enough room in the toe-box, heel, and arch of the shoe. All of these features provide you with the very best in comfort and help prevent potential foot complications.</p>
  </div>
  <div class="faq-item" style="top:440px">How Do You Know If Orthopedic Shoes Are Right For You?</div>
  <div class="faq-photo" role="img" aria-label="Blue canvas sneaker on a light background"></div>
</section>

<section class="catalog">
  <h2>Request a Free Diabetic Shoe Catalog</h2>
  <div class="field" style="left:88px;top:150px;width:320px">First name:</div>
  <div class="field" style="left:440px;top:150px;width:320px">Last name:</div>
  <div class="field" style="left:788px;top:150px;width:324px">Address name:</div>
  <div class="field" style="left:88px;top:207px;width:320px">City:</div>
  <div class="field" style="left:440px;top:207px;width:320px">State:</div>
  <div class="field" style="left:788px;top:207px;width:324px">Zip:</div>
  <div class="field" style="left:88px;top:264px;width:320px">Phone:</div>
  <div class="field" style="left:440px;top:264px;width:320px">Best Time Of Call:</div>
  <div class="field" style="left:788px;top:264px;width:324px">Email:</div>
  <div class="field select" style="left:88px;top:320px;width:500px">Primary Insurance:</div>
  <div class="field select" style="left:610px;top:320px;width:502px">Do you want to check eligibility Online?</div>
  <div class="field" style="left:88px;top:373px;width:1024px">Comments:</div>
  <div class="btn">Request Catalog</div>
</section>

<footer class="bottombar">
  <div class="copy">© Pebble Walk Co - All Rights Reserved, Co-payments, deductibles and some restrictions apply.</div>
  <div class="links">Terms of Use Privacy Policy Returns/Exchanges</div>
</footer>
<div class="totop"><svg width="12" height="8"><path d="M1 7l5-5 5 5" fill="none" stroke="#fff" stroke-width="1.5"/></svg></div>

</div>
</body>
</html>
```